Online Advertising agency with fun music culture twist

We need a new website for our online advertising agency. The current site is just a placeholder but you can pull the text from the site- quillmarketbench.com. The new site will be 10 total pages. The current site has 8 pages. So this project will require the design and code for all 10 pages.

Things I like- Clean, easy to read, custom graphics, video,
splash 1-2 colors, futuristic, music twist, fun, interesting, looks amazing on a mobile site, extremely professional design.

Things I don't like- I hate stock graphics, pages that scroll to much, to many colors (rainbow), sites that don't flow, very templated cookie cutter sites, not mobile compliant.

We built a sophisticated buying platform for advertisers to reach the right person on the right device at the right time. I used to be a concert promoter and I have several musicians that work with us. We want to play into the fun and excitement of live music with an advertising twist hence the name Quill. We don't want to make it seem like a music company but we can use subtle vinyl and music references. My other company is meadowpixelworks.com for reference. I really like to design of my other company.

Target Market(s)

Online websites and fortune 500 advertisers- You can see my other company at meadowpixelworks.com

Industry/Entity Type

Advertising

Coding

Coded - Design and coding required

Number of Pages Required

5+ page

Font styles to use
Other font styles liked:
• Be creative

Requirements
Must have
• HTML5, Clean, easy to read, custom graphics, use of video graphics,
• splash 1-2 colors, futuristic, music twist, fun, interesting, looks amazing on a mobile site, extremely professional design. Play into the music theme, vinyl records etc
Nice to have
• Video, interactivity, custom build (not a template)
Should not have
• Flash. I hate stock photos, pages that scroll to much, to many colors (rainbow), sites that don't flow, very templated cookie cutter sites, not mobile compliant.

```html
<!DOCTYPE html>
<html lang="en">
<head>
<meta charset="utf-8">
<title>Quill Trading Desk</title>
<link href="https://fonts.googleapis.com/css2?family=Montserrat:wght@400;500;600;700&family=Lato:wght@400;700&display=swap" rel="stylesheet">
<style>
:root{
  --orange:#f0913a;
  --brown:#5a3a1c;
  --ink:#222222;
  --nav:#262626;
  --footer:#1e1e1e;
  --light:#f4f4f4;
  --muted:#8a8a8a;
  --line:#e4e4e4;
  --white:#ffffff;
}
*{margin:0;padding:0;box-sizing:border-box}
html,body{width:850px;height:1200px;overflow:hidden;background:var(--white)}
body{position:relative;font-family:'Montserrat',sans-serif;color:var(--ink)}
.abs{position:absolute}

/* hero */
.hero{left:0;top:0;width:850px;height:396px;background:radial-gradient(ellipse at 45% 70%,#2a2520 0%,#1a1a1a 45%,#0f0f0f 100%)}
.hero-brand{left:0;top:130px;width:850px;text-align:center}
.hero-brand .name{font-weight:700;font-size:44px;letter-spacing:4px;color:#cfcfcf;line-height:1}
.hero-brand .sub{font-weight:700;font-size:12px;letter-spacing:5px;color:#cfcfcf;margin-top:6px}
.hero-title{left:0;top:203px;width:850px;text-align:center;color:var(--white);font-weight:700;font-size:14.5px;line-height:20px;letter-spacing:.3px}
.btn-orange{background:var(--orange);color:var(--white);font-weight:600;font-size:8px;letter-spacing:.3px;display:flex;align-items:center;justify-content:center;gap:5px}
.hero-btn{left:368px;top:258px;width:109px;height:25px}
.slide-arrow{top:199px;width:36px;height:37px;display:flex;align-items:center;justify-content:center}
.slide-arrow.prev{left:0;background:var(--brown)}
.slide-arrow.next{left:813px;background:#050505}

/* nav */
.nav{left:0;top:396px;width:850px;height:40px;background:var(--nav)}
.nav a{position:absolute;top:0;height:40px;line-height:40px;color:var(--white);font-weight:600;font-size:8px;text-decoration:none}
.nav a.active{background:var(--orange);width:50px;text-align:center}
.nav .divider{position:absolute;left:689px;top:8px;width:1px;height:24px;background:#444}
.nav .search{position:absolute;left:705px;top:12px}

/* intro */
.intro{left:0;top:436px;width:850px;height:224px;background:var(--light)}
.section-title{left:0;width:850px;text-align:center;font-weight:700;font-size:18px;letter-spacing:.3px;color:var(--ink)}
.intro-text{left:143px;top:82px;width:566px;text-align:center;font-family:'Lato',sans-serif;font-size:7.7px;line-height:12.5px;color:var(--muted)}
.btn-plain{left:342px;top:166px;width:162px;height:25px;background:var(--white);border:1px solid var(--line);font-weight:500;font-size:8px;display:flex;align-items:center;justify-content:center}

/* services */
.services{left:0;top:660px;width:850px;height:220px;background:var(--white)}
.service{top:65px;width:132px;height:92px;border:1px solid var(--line);box-shadow:0 0 0 2px #f6f6f6;text-align:center}
.service .icon{margin-top:22px;height:28px}
.service .label{font-weight:500;font-size:7.6px;margin-top:8px}
.service .tab{position:absolute;left:52px;bottom:-9px;width:28px;height:16px;background:var(--white);border:1px solid var(--line);display:flex;align-items:center;justify-content:center}
.service.featured{background:var(--orange);border-color:var(--orange);color:var(--white)}
.service.featured .tab{background:var(--ink);border-color:var(--ink)}

/* cta */
.cta{left:0;top:880px;width:850px;height:85px;background:var(--ink)}
.cta-text{left:157px;top:33px;color:var(--white);font-weight:600;font-size:15.5px;letter-spacing:.2px}
.cta-btn{left:572px;top:30px;width:145px;height:27px}

/* partners */
.partners{left:0;top:965px;width:850px;height:167px;background:var(--white)}
.partner{top:100px;height:36px;display:flex;align-items:center;justify-content:center;gap:5px;font-weight:700;font-size:15px;color:#4a4a4a}

/* footer */
.footer{left:0;top:1132px;width:850px;height:68px;background:var(--footer)}
.footer-links{left:132px;top:24px;font-family:'Lato',sans-serif;font-size:7px;color:#d8d8d8}
.footer-links span.sep{color:#666;margin:0 7px}
.copyright{left:132px;top:39px;font-family:'Lato',sans-serif;font-size:6.3px;color:#8a8a8a}
.social{top:24px;width:20px;height:20px;border-radius:50%;background:#2c2c2c;display:flex;align-items:center;justify-content:center}
.social i{display:block;width:7px;height:7px;border-radius:50%;background:#e8e8e8}
</style>
</head>
<body>

<section class="abs hero" role="img" aria-label="Dark faceted low-poly background with a warm amber glow"></section>
<div class="abs hero-brand">
  <div class="name">QUILL</div>
  <div class="sub">TRADING DESK</div>
</div>
<h1 class="abs hero-title">ADVERTISING MADE EASY<br>WITH A UNIFIED BUYING PLATFORM</h1>
<div class="abs btn-orange hero-btn">READ MORE
  <svg width="10" height="10" viewBox="0 0 10 10"><circle cx="5" cy="5" r="4.2" fill="none" stroke="#fff" stroke-width="1.2"/><path d="M3 5h3.6M5.2 3.4L6.8 5 5.2 6.6" fill="none" stroke="#fff" stroke-width="1.1"/></svg>
</div>
<div class="abs slide-arrow prev"><svg width="8" height="10" viewBox="0 0 8 10"><path d="M5.5 2L2.5 5l3 3" fill="none" stroke="#fff" stroke-width="1.4"/></svg></div>
<div class="abs slide-arrow next"><svg width="8" height="10" viewBox="0 0 8 10"><path d="M2.5 2l3 3-3 3" fill="none" stroke="#fff" stroke-width="1.4"/></svg></div>

<nav class="abs nav">
  <a class="active" style="left:132px">HOME</a>
  <a style="left:204px">ADVERTISERS</a>
  <a style="left:292px">PUBLISHERS</a>
  <a style="left:374px">ABOUT US</a>
  <span class="divider"></span>
  <svg class="search" width="14" height="14" viewBox="0 0 14 14"><circle cx="6" cy="6" r="4.3" fill="none" stroke="#fff" stroke-width="1.5"/><path d="M9.2 9.2L12.5 12.5" stroke="#fff" stroke-width="1.6"/></svg>
</nav>

<section class="abs intro">
  <h2 class="abs section-title" style="top:48px">GLOBAL SCALE WITH ROI TOP OF MIND</h2>
  <p class="abs intro-text">Our technology and services enable marketers to connect with the audiences they want at the scale they need to achieve the outcomes they desire. Lorem ipsum dolor sit amet, consectetur adipiscing elit. Maecenas ultricies neque et aliquam scelerisque. Etiam euismod fringilla neque, id blandit felis porttitor vel. Curabitur ligula metus, lobortis non varius et, ultricies id turpis. Curabitur eget nisl at purus consequat dapibus. Quisque non magna vehicula, posuere lorem nec, hendrerit neque. Phasellus bibendum arcu erat, id lobortis sem cursus quis. Ut dapibus condimentum turpis, nec semper dui bibendum consectetur. Sed non elementum mi. Aenean malesuada lobortis leo, non sodales ante mollis ut.</p>
  <div class="abs btn-plain">MORE ABOUT US</div>
</section>

<section class="abs services">
  <h2 class="abs section-title" style="top:22px">OUR SERVICES</h2>

  <div class="abs service" style="left:140px">
    <div class="icon"><svg width="26" height="20" viewBox="0 0 26 20"><rect x="4" y="2" width="18" height="12" rx="1" fill="none" stroke="#222" stroke-width="1.8"/><path d="M1 16h24v1.5H1z" fill="#222"/></svg></div>
    <div class="label">CROSS-CHANNEL TARGETING</div>
    <div class="tab"><svg width="9" height="8" viewBox="0 0 9 8"><path d="M1 1h3v1.2H2.2v3.6H4V7H1z M4 2.5h2.5V1L9 4 6.5 7V5.5H4z" fill="#222"/></svg></div>
  </div>

  <div class="abs service featured" style="left:286px">
    <div class="icon"><svg width="28" height="26" viewBox="0 0 28 26"><g fill="#fff"><circle cx="10" cy="15" r="7"/><circle cx="21" cy="7" r="5"/><circle cx="21" cy="20" r="4"/></g><g fill="#f0913a"><circle cx="10" cy="15" r="2.6"/><circle cx="21" cy="7" r="1.8"/><circle cx="21" cy="20" r="1.4"/></g></svg></div>
    <div class="label">AUTOMATED BUYING</div>
    <div class="tab"><svg width="9" height="8" viewBox="0 0 9 8"><path d="M1 1h3v1.2H2.2v3.6H4V7H1z M4 2.5h2.5V1L9 4 6.5 7V5.5H4z" fill="#fff"/></svg></div>
  </div>

  <div class="abs service" style="left:432px">
    <div class="icon"><svg width="20" height="28" viewBox="0 0 20 28"><path d="M2 1h11l5 5v21H2z" fill="none" stroke="#222" stroke-width="1.6"/><path d="M13 1v5h5" fill="none" stroke="#222" stroke-width="1.4"/><path d="M5 12h10M5 16h10M5 20h10" stroke="#222" stroke-width="1.4"/></svg></div>
    <div class="label">FULL TRANSPARENCY</div>
    <div class="tab"><svg width="9" height="8" viewBox="0 0 9 8"><path d="M1 1h3v1.2H2.2v3.6H4V7H1z M4 2.5h2.5V1L9 4 6.5 7V5.5H4z" fill="#222"/></svg></div>
  </div>

  <div class="abs service" style="left:578px">
    <div class="icon"><svg width="28" height="26" viewBox="0 0 28 26"><g fill="#222"><circle cx="14" cy="7" r="4.5"/><circle cx="6" cy="9" r="3.5"/><circle cx="22" cy="9" r="3.5"/><path d="M7 25c0-7 3-11 7-11s7 4 7 11z"/><path d="M0 21c0-5 2-8 6-8 1.5 0 2.5.5 3 1-1.5 2-2.5 4.5-2.5 7z"/><path d="M28 21c0-5-2-8-6-8-1.5 0-2.5.5-3 1 1.5 2 2.5 4.5 2.5 7z"/></g></svg></div>
    <div class="label">TRUE PARTNERSHIPS</div>
    <div class="tab"><svg width="9" height="8" viewBox="0 0 9 8"><path d="M1 1h3v1.2H2.2v3.6H4V7H1z M4 2.5h2.5V1L9 4 6.5 7V5.5H4z" fill="#222"/></svg></div>
  </div>
</section>

<section class="abs cta">
  <p class="abs cta-text">Praesent facilisis nisi sed neque fermentum</p>
  <div class="abs btn-orange cta-btn">CONTACT NOW
    <svg width="11" height="11" viewBox="0 0 10 10"><circle cx="5" cy="5" r="4.2" fill="none" stroke="#fff" stroke-width="1.1"/><path d="M3 5h3.6M5.2 3.4L6.8 5 5.2 6.6" fill="none" stroke="#fff" stroke-width="1"/></svg>
  </div>
</section>

<section class="abs partners">
  <h2 class="abs section-title" style="top:42px">DELIVERING VALUE TO OUR PARTNERS...</h2>
  <div class="abs partner" style="left:150px;width:110px">Harlow Denim</div>
  <div class="abs partner" style="left:240px;width:100px">Marlowe's</div>
  <div class="abs partner" style="left:350px;width:150px;font-size:18px">Hearth&amp;Hollow</div>
  <div class="abs partner" style="left:510px;width:120px">Summit Lending</div>
  <div class="abs partner" style="left:650px;width:44px"><svg width="38" height="38" viewBox="0 0 38 38" role="img" aria-label="Partner badge"><circle cx="19" cy="19" r="17" fill="none" stroke="#3bb0c0" stroke-width="2"/></svg></div>
</section>

<footer class="abs footer">
  <div class="abs footer-links">Home<span class="sep">/</span>About<span class="sep">/</span>Privacy Policy<span class="sep">/</span>Terms &amp; Conditions<span class="sep">/</span>Contact</div>
  <div class="abs copyright">Copyright(c) 2016 website name, All Rights Reserved.</div>
  <div class="abs social" style="left:572px" aria-label="Video channel"><i></i></div>
  <div class="abs social" style="left:597px" aria-label="Photo channel"><i></i></div>
  <div class="abs social" style="left:622px" aria-label="Email"><svg width="10" height="8" viewBox="0 0 10 8"><rect x="0.5" y="0.5" width="9" height="7" fill="#e8e8e8"/><path d="M0.5 0.8L5 4.5 9.5 0.8" fill="none" stroke="#2c2c2c" stroke-width="1"/></svg></div>
  <div class="abs social" style="left:647px" aria-label="Professional network"><i></i></div>
  <div class="abs social" style="left:672px" aria-label="Microblog"><i></i></div>
  <div class="abs social" style="left:697px" aria-label="Social network"><i></i></div>
</footer>

</body>
</html>
```